RPM/CCM Marketing Book

We need a new logo designed for the company,
Bramford Diagnostics, some logo ideas are attached.

We would like this book revamped with a new design as well as included updates made in line with the design and text. Please let me know of any clarifications or follow-up questions that possible can come up. The old booklet is attached as well which is to be used for the new design.

```html
<!DOCTYPE html>
<html lang="en">
<head>
<meta charset="utf-8">
<title>Bramford Diagnostics – RPM/CCM Marketing Book</title>
<link href="https://fonts.googleapis.com/css2?family=Roboto:wght@400;500;700;900&display=swap" rel="stylesheet">
<style>
:root{
  --stage:#2b2b2b;
  --paper:#ffffff;
  --blue:#2aa3dc;
  --navy:#1f3b57;
  --grey:#dcdfe3;
  --grey-mid:#9aa3ad;
  --ink:#333a42;
  --text-muted:#6c747d;
}
*{box-sizing:border-box;margin:0;padding:0}
html,body{width:672px;height:1200px;overflow:hidden;background:var(--stage);font-family:'Roboto',sans-serif;color:var(--ink)}
.board{position:relative;width:672px;height:1200px}
.page{position:absolute;background:var(--paper);overflow:hidden}

/* cover */
.cover{left:340px;top:40px;width:278px;height:412px}
.brand{display:flex;align-items:center;gap:5px;font-weight:700;color:var(--navy);font-size:9px;line-height:1.1;text-transform:uppercase}
.brand .mark{width:12px;height:12px;background:var(--blue);border-radius:50%;flex:none}
.cover .brand{position:absolute;left:20px;top:16px}
.cover-photo{position:absolute;left:0;top:52px;width:278px;height:200px;background:linear-gradient(135deg,#eef1f4,#c9d2da 60%,#8b9aa8)}
.cover-band{position:absolute;left:78px;top:252px;width:200px;height:48px;background:var(--blue);color:#fff;padding:9px 10px}
.cover-band h1{font-size:10px;font-weight:900;letter-spacing:0;white-space:nowrap}
.cover-band p{font-size:9.5px;font-weight:500;margin-top:4px}
.cover-lower{position:absolute;left:0;top:300px;width:278px;height:112px;background:linear-gradient(160deg,#f3f4f6,var(--grey))}
.cover-url{position:absolute;right:14px;bottom:14px;font-size:8px;color:var(--blue);font-weight:500}

/* contents spread */
.contents{left:54px;top:480px;width:564px;height:282px}
.contents-photo{position:absolute;left:0;top:0;width:300px;height:282px;background:linear-gradient(120deg,#e8edf1,#bcd3e4 55%,#2b7fb8)}
.contents-wedge{position:absolute;left:0;top:0}
.contents-title{position:absolute;left:300px;top:36px;color:var(--navy);font-size:14px;font-weight:900;line-height:1.15;width:80px}
.toc{position:absolute;left:380px;top:30px;width:168px;list-style:none;font-size:5.4px;line-height:1}
.toc li{display:flex;justify-content:space-between;border-bottom:1px dotted #c5cbd1;padding:2.4px 0;color:var(--text-muted)}
.toc li.main{color:var(--blue);font-weight:700}
.toc li.sub{padding-left:8px}
.spine{position:absolute;left:282px;top:0;width:1px;height:282px;background:rgba(0,0,0,.08)}

/* case spread */
.case{left:54px;top:784px;width:564px;height:381px}
.case-left{position:absolute;left:0;top:0;width:282px;height:381px;padding:16px 14px}
.case-left .brand{font-size:6px}
.case-left .brand .mark{width:9px;height:9px}
.case h2{font-size:20px;font-weight:900;color:var(--navy);margin-top:10px;display:flex;align-items:center;gap:6px}
.case h2 .tag{background:var(--blue);color:#fff;font-size:11px;padding:3px 8px}
.case .lede{font-size:7.5px;font-weight:700;color:var(--navy);margin-top:4px;line-height:1.3}
.compare{width:254px;border-collapse:collapse;margin-top:10px;font-size:5px;line-height:1.35;color:var(--text-muted)}
.compare th{background:var(--blue);color:#fff;text-align:left;padding:3px 4px;font-size:5.6px}
.compare td{vertical-align:top;padding:3px 4px;border-bottom:1px solid var(--grey)}
.benefits{margin-top:10px}
.benefits h3{font-size:8px;color:var(--navy);font-weight:900}
.benefits h3 span{color:var(--blue)}
.benefits ol{margin:4px 0 0 10px;font-size:5.4px;line-height:1.6;color:var(--text-muted)}
.case-right{position:absolute;left:282px;top:0;width:282px;height:381px;padding:16px 14px}
.case-right .brand{justify-content:flex-end;font-size:6px}
.case-right .brand .mark{width:9px;height:9px}
.case-right h2{color:var(--blue);font-size:18px}
.steps{display:grid;grid-template-columns:1fr 1fr;gap:3px 10px;margin-top:8px;font-size:5px;line-height:1.4;color:var(--text-muted);list-style:none}
.steps li::before{content:"• ";color:var(--blue)}
.case-photo{margin-top:10px;width:160px;height:82px;background:linear-gradient(135deg,#d9dee4,#8c99a8)}
.case-foot{position:absolute;left:282px;bottom:0;width:282px;height:70px;background:var(--grey);padding:10px 14px;font-size:4.6px;line-height:1.5;color:var(--text-muted);columns:2;column-gap:10px}
</style>
</head>
<body>
<div class="board">

  <section class="page cover">
    <div class="brand"><span class="mark"></span><span>Bramford Diagnostics</span></div>
    <div class="cover-photo" role="img" aria-label="Doctor in white coat at a laptop holding a video consultation"></div>
    <div class="cover-lower"></div>
    <div class="cover-band"><h1>RPM/CCM/RTM/CPM/BHI/TCM/PCM</h1><p>2023</p></div>
    <div class="cover-url">www.bramforddiag.com</div>
  </section>

  <section class="page contents">
    <div class="contents-photo" role="img" aria-label="Smiling nurse with stethoscope in blue scrubs, colleague behind"></div>
    <svg class="contents-wedge" width="564" height="282" aria-hidden="true"><polygon points="300,0 360,0 330,282 300,282" fill="#f1f3f5"/></svg>
    <div class="spine"></div>
    <h2 class="contents-title">TABLE OF CONTENTS</h2>
    <ol class="toc">
      <li class="main"><span>The Case for Remote Patient Monitoring</span><span>3</span></li>
      <li class="main"><span>How to Get Started</span><span>4</span></li>
      <li class="main"><span>Chronic Care Management (CCM)</span><span>5</span></li>
      <li class="sub"><span>Who qualifies for CCM</span><span>5</span></li>
      <li class="sub"><span>CCM Eligible Conditions</span><span>6</span></li>
      <li class="sub"><span>CCM Billing Codes</span><span>6</span></li>
      <li class="sub"><span>Benefits to Patients</span><span>7</span></li>
      <li class="sub"><span>Benefits to Practices</span><span>7</span></li>
      <li class="main"><span>Remote Patient Monitoring (RPM)</span><span>8</span></li>
      <li class="sub"><span>Who qualifies for RPM</span><span>8</span></li>
      <li class="sub"><span>RPM Devices</span><span>9</span></li>
      <li class="sub"><span>RPM Billing Codes</span><span>9</span></li>
      <li class="sub"><span>Reimbursement Rates</span><span>10</span></li>
      <li class="sub"><span>RPM Workflow Overview</span><span>10</span></li>
      <li class="sub"><span>Remote Therapeutic Monitoring</span><span>11</span></li>
      <li class="sub"><span>Principal Care Management</span><span>11</span></li>
      <li class="sub"><span>Behavioral Health Integration</span><span>12</span></li>
      <li class="sub"><span>Transitional Care Management</span><span>12</span></li>
      <li class="main"><span>Frequently Asked Questions</span><span>13</span></li>
      <li class="sub"><span>RPM Questions</span><span>13</span></li>
      <li class="sub"><span>CCM Questions</span><span>14</span></li>
    </ol>
  </section>

  <section class="page case">
    <div class="case-left">
      <div class="brand"><span class="mark"></span><span>Bramford Care LLC</span></div>
      <h2>The Case for <span class="tag">Outsourcing</span></h2>
      <p class="lede">Remote Patient Monitoring/Chronic Care Management<br>by a trusted 3rd party Bramford Care LLC</p>
      <table class="compare">
        <tr><th>CCM</th><th>RPM</th></tr>
        <tr><td>Monthly care plan calls keep patients engaged between office visits and lower readmissions.</td><td>Connected devices send daily readings so staff can act before issues grow.</td></tr>
        <tr><td>Our nurses handle outreach, documentation and time tracking for each patient.</td><td>We supply devices, train patients and review data every business day.</td></tr>
        <tr><td>Practices bill monthly codes with no added staff or overhead cost.</td><td>Alerts reach your providers quickly with clear, ready summaries.</td></tr>
      </table>
      <div class="benefits">
        <h3><span>MEDICAL</span> Offices Benefits:</h3>
        <ol>
          <li>New monthly revenue from existing patients.</li>
          <li>Better outcomes and fewer hospital visits.</li>
          <li>No hiring, training or extra staff time.</li>
          <li>Complete billing reports each month.</li>
          <li>Improved patient satisfaction scores.</li>
        </ol>
      </div>
    </div>
    <div class="case-right">
      <div class="brand"><span>www.bramforddiag.com</span><span class="mark"></span></div>
      <h2>How to Get Started:</h2>
      <ul class="steps">
        <li>Schedule a short call with our team to review your practice.</li>
        <li>We identify eligible patients from your current lists.</li>
        <li>Sign a simple service agreement with no setup fee.</li>
        <li>Our nurses enroll patients and explain the program.</li>
        <li>Devices ship directly to patient homes.</li>
        <li>Readings and calls are logged in your records.</li>
        <li>Monthly reports are sent for easy billing.</li>
        <li>Your staff gets ongoing support at any time.</li>
      </ul>
      <div class="case-photo" role="img" aria-label="Care coordinator speaking with a patient at a desk"></div>
    </div>
    <div class="case-foot">Program details depend on payer rules and patient eligibility. Billing codes and rates are reviewed each year and may change. Contact our team for current figures and guidance for your practice and region.</div>
  </section>

</div>
</body>
</html>
```